Wordpress Theme for Medical Clinics

** Please view updated Sitemap2.pdf doc to clarify some confusion ***

This is a multiuser WordPress subscription site for medical clinics. Please see attachment for sitemap. Please do not include extra content like social media icons, search bars, or images. If you have questions, please ask for clarification.
The site contains the following pages and sub-pages:

1. Home
2. Our Clinic
2a. Our Clinic > Mission
2b. Our Clinic > Services
2c. Our Clinic > Clinic Policies
2d. Our Clinic > Schedules
3. Our Staff
3a. Our Staff > [Staff member page]
4. Resources
4a. Resources > Patient Health (index)
4b. Resources > Patient Health (index) > [post]
4c. Resources > Links
4d. Resources > Forms
5. Alerts
5a. Alerts > [Alert Page]
6. Contact Us

Includes the Following Pages, Subpages, and Content
1. Home
a. About Us
b. Our Staff
c. Bulletins
d. Accepting New Patients (shown as an alert widget)
e. Links
i. Physician Toolbox
ii. Book an Appointment
f. Clinic Policies
i. Show first 3 policies (e.g. Late Arrivals, Missed Appointments, Fees)
ii. Link to Clinic Policies page
g. Primary widget (displayed on all pages)
i. Hours of operation
ii. Contact Info
1. Tel
2. Fax
3. Email
4. Address
5. Get directions (link to Google Maps)
2. Our Clinic
a. Main Page
i. Clinic Name
ii. Overview
iii. Languages Spoken
iv. Secondary Navigation
1. Mission
2. Services
3. Clinic Policies
4. Schedules (see attachment)
b. Our Clinic > Mission
c. Our Clinic > Services
i. For each service include service TITLE and DESCRIPTION
d. Our Clinic > Clinic Policies
i. For each policy include policy TITLE and DESCRIPTION
ii. Include the following policies in mockup
1. Late arrivals
2. Missed appointments
3. Fees for missed appointments
4. Referrals and follow-ups
5. Services not covered by RHC
6. Information for LTA patients
7. Medical Legal Reports
e. Our Clinic > Schedules
3. Our Staff
a. Main Page
i. Display a list of staff members. Include NAME and DESIGNATION
b. Our Staff > [Staff Name]
i. Include NAME, PICTURE, DESIGNATION, and BIO
4. Resources
a. Resources > Patient Health
i. Main Page
1. Posts (ordered by date)
a. Title
b. Summary
2. Side Navigation
a. Post Categories
ii. Patient Health > [post title]
1. Title
2. Post Category
3. Date
4. Author
5. Summary
6. Body
b. Resources > Links
1. Secondary Navigation - Categories
a. Sample Categories:
i. Local Services
ii. RHC and Drug Coverage
iii. Mental Health Resources
2. Category page
a. Include the following links in the 'Local Services' category
i. Hypertension clinics
ii. Home Care services
iii. Vaccine Clinics
c. Resources > Forms
i. Display a table with form TITLE and CATEGORY
ii. Side Navigation
1. Form Categories
a. Use the following sample Categories
i. Referrals
ii. Insurance
iii. Intake
iv. Discharge
v. Waivers
5. Alerts
a. Main page
i. List of all Alert posts
1. Include post TITLE as a link to the post
ii. Side Navigation
1. Alerts Archive
a. shown as Month + Number of posts
iii. Alerts > [Alert page]
1. Include TITLE, DATE, AUTHOR, BODY
6. Contact Us
a. Map
b. Hours of operation
c. Address
d. Phone number
e. Fax number
e. Fax number
f. Map
g. Email

Design notes:
- fixed width
- responsive (need designs for mobile, tablet, and desktop)
- simple, dark font, white background
- use Font Awesome icons where needed
- user adds own logo

Medical Clinics

Medical

5+ page

Serif
Sans Serif

• Please keep designs very simple.
• Examples:
• https://www.plovana.com/install
• http://www.quendrix.com/company/about-us
• http://brightumtally.org/
• http://www.norp.com/
• Minimal or no use of shadows and gradients

```html
<!DOCTYPE html>
<html lang="en">
<head>
<meta charset="utf-8">
<title>Clinic Name – Quality Care</title>
<link rel="stylesheet" href="https://fonts.googleapis.com/css2?family=Dosis:wght@400;500;600;700&family=Montserrat:wght@400&display=swap">
<style>
:root{
  --navy:#2e4470;
  --navy-deep:#233656;
  --blue:#2196f3;
  --blue-light:#55aaf3;
  --blue-table:#1f8ef0;
  --page:#f7f7f7;
  --card:#ececec;
  --text:#2e3a52;
  --muted:#8a8f99;
  --white:#ffffff;
}
*{margin:0;padding:0;box-sizing:border-box}
html,body{width:782px;height:1200px;overflow:hidden}
body{position:relative;background:var(--page);font-family:"Dosis",sans-serif;color:var(--text)}
.abs{position:absolute}
a{color:inherit;text-decoration:none}

/* header */
.site-header{left:0;top:0;width:782px;height:34px;background:var(--navy)}
.brand{left:75px;top:4px;font-size:21px;font-weight:700;color:var(--white)}
.main-nav{left:342px;top:10px;font-size:12.5px;color:var(--white)}
.main-nav a{position:absolute;white-space:nowrap}
.nav-contact{left:615px;top:7px;width:94px;height:22px;background:#4aa8f5;border-radius:3px;color:var(--white);font-size:13px;text-align:center;line-height:22px}

/* hero */
.hero-photo{left:0;top:34px;width:782px;height:278px;background:linear-gradient(90deg,#c9dbe8 0%,#e8eff4 25%,#a9c8e2 55%,#7fb0db 100%)}
.hero-title{left:397px;top:103px;font-size:35px;font-weight:600;color:var(--white);letter-spacing:1.5px;white-space:nowrap}
.hero-sub{left:397px;top:142px;font-size:23px;color:var(--white);letter-spacing:1.5px;white-space:nowrap}
.hero-text{left:396px;top:178px;width:246px;font-size:11.5px;line-height:16.5px;color:var(--white)}
.hero-btn{left:391px;top:241px;width:134px;height:26px;background:var(--navy);border-radius:3px;color:var(--white);font-size:11.5px;text-align:center;line-height:26px}

/* about */
.section-title{font-size:19px;font-weight:500;color:var(--text)}
.about-photo{left:81px;top:370px;width:219px;height:165px;background:linear-gradient(135deg,#cfe0ec,#8fb6d6 60%,#5b8fbf)}
.about-text{left:313px;top:368px;width:172px;font-family:"Montserrat",sans-serif;font-size:8.3px;line-height:11px;color:var(--muted)}
.about-text p+p{margin-top:6px}
.btn-outline{left:311px;top:518px;width:47px;height:17px;border:1px solid var(--navy);border-radius:3px;font-size:7.5px;font-weight:600;text-align:center;line-height:15px;color:var(--navy);background:var(--white)}

/* hours */
.hours-panel{left:488px;top:312px;width:221px;height:247px;background:var(--blue-light)}
.hours-title{left:504px;top:333px;font-size:19px;font-weight:400;color:var(--white)}
.hours-table{left:496px;top:361px;width:205px;height:153px;background:var(--blue-table);color:var(--white);font-size:11px;border-collapse:collapse}
.hours-table td{height:21.8px;padding:0}
.hours-table td:first-child{padding-left:8px;width:94px}
.hours-table td.dash{width:20px;text-align:center}
.btn-appointment{left:531px;top:519px;width:135px;height:29px;border:2px solid var(--white);border-radius:4px;background:linear-gradient(#1e6fd0,#0d4fa8);color:var(--white);font-size:11px;text-align:center;line-height:25px}

/* cards */
.card{background:var(--card)}
.card-head{position:relative;height:35px;padding-left:13px;font-size:19px;line-height:35px;color:var(--white)}
.head-blue{background:var(--blue)}
.head-navy{background:var(--navy)}
.card-icon{position:absolute;right:10px;top:7px}
.staff-list{list-style:none;margin:12px 17px 0 13px;font-size:10.5px;font-weight:500}
.staff-list li{border-bottom:1px solid #b5b8bd;height:18.5px;line-height:20px}
.staff-list li:last-child{border-bottom:none}
.link-list{list-style:none;margin:8px 0 0 12px;font-size:10.5px}
.link-list li{height:19.7px;line-height:19px;display:flex;align-items:center;gap:5px}
.btn-small{position:absolute;height:18px;border-radius:3px;color:var(--white);font-size:9px;text-align:center;line-height:18px}
.btn-blue{background:var(--blue)}
.btn-sky{background:#5fb3f5}

.newpatients{left:506px;top:594px;width:203px;height:89px;background:var(--navy);color:var(--white)}
.newpatients h3{position:absolute;left:11px;top:9px;font-size:19px;font-weight:500}
.newpatients p{position:absolute;left:11px;top:37px;font-size:11px}
.btn-contact{left:7px;top:61px;width:78px;height:20px;background:var(--navy-deep);border-radius:3px;font-size:9px;text-align:center;line-height:20px}
.toolbox-panel{left:506px;top:694px;width:203px;height:93px;background:var(--blue)}
.btn-toolbox{left:25px;top:31px;width:151px;height:31px;border:2px solid var(--white);border-radius:4px;background:linear-gradient(#1e6fd0,#0d4fa8);color:var(--white);font-size:13px;text-align:center;line-height:27px}

.alerts-card{left:81px;top:802px;width:408px;height:212px}
.alerts-card .card-head{height:41px;line-height:41px;padding-left:11px}
.alert-item{position:absolute;left:12px;width:370px}
.alert-item h4{font-size:11.5px;font-weight:500;margin-bottom:7px}
.alert-item p{font-family:"Montserrat",sans-serif;font-size:8.3px;line-height:10.8px;color:var(--muted)}

.policies-card{left:506px;top:802px;width:203px;height:212px}
.policies-card .card-head{height:41px;line-height:38px;padding-left:11px}
.policy-list{list-style:none;margin:10px 0 0 13px;font-size:10px}
.policy-list li{height:17.9px}

/* footer */
.site-footer{left:0;top:1035px;width:782px;height:165px;background:var(--navy);color:var(--white)}
.footer-col h5{font-size:13.5px;font-weight:500;margin-bottom:9px}
.footer-col ul{list-style:none;font-size:11px;color:#aeb8cc}
.footer-col ul li{height:18.3px}
.footer-rule{position:absolute;top:36px;width:1px;height:106px;background:#4a5f89}
.footer-hours{font-size:7.5px;color:#c8d0e0;border-collapse:collapse}
.footer-hours td{height:15.2px;padding:0}
.footer-hours td:first-child{width:68px}
.footer-contact{list-style:none;font-size:11px;color:#aeb8cc}
.footer-contact li{height:20.5px;display:flex;align-items:center;gap:4px;white-space:nowrap}
.copyright{left:87px;top:147px;font-size:8px;color:#8894ad}
</style>
</head>
<body>

<header class="site-header abs">
  <div class="brand abs">Clinic Name</div>
  <nav class="main-nav abs">
    <a style="left:0">Home</a>
    <a style="left:51px">Our Clinic</a>
    <a style="left:116px">Staff</a>
    <a style="left:162px">Resources</a>
    <a style="left:232px">Alerts</a>
  </nav>
  <a class="nav-contact abs">Contact us</a>
</header>

<section>
  <div class="hero-photo abs" role="img" aria-label="Senior doctor using a tablet in a bright hospital hallway"></div>
  <h1 class="hero-title abs">Quality Care</h1>
  <div class="hero-sub abs">Provided For everyone!</div>
  <p class="hero-text abs">Highly skilled and Experienced medical staff comfortable and cosy patient rooms,state-of-theart dianostic equipment.</p>
  <a class="hero-btn abs">Book an Appointment</a>
</section>

<section>
  <h2 class="section-title abs" style="left:82px;top:333px">Our Clinic</h2>
  <div class="about-photo abs" role="img" aria-label="Doctor and nurse standing in a clinic corridor"></div>
  <div class="about-text abs">
    <p>Lorem ipsum dolor sit amet, consectetuer adipiscing elit, sed diam nonummy nibh euismod tincidunt ut laoreet dolore magna aliquam erat volutpat. Ut wisi enim ad minim veniam, quis nostrud exerci tation ullamcorper suscipit lobortis nisl ut aliquip ex ea commodo consequat.</p>
    <p>Ut wisi enim ad minim veniam, quis nostrud exerci tation ullamcorper suscipit lobortis nisl ut aliquip ex ea commodo consequat.</p>
  </div>
  <a class="btn-outline abs">Learn More</a>
</section>

<aside>
  <div class="hours-panel abs"></div>
  <h2 class="hours-title abs">Hours of operation</h2>
  <svg class="abs" style="left:677px;top:332px" width="23" height="23" viewBox="0 0 24 24" aria-hidden="true">
    <circle cx="12" cy="12" r="10.5" fill="none" stroke="#fff" stroke-width="1.6"/>
    <circle cx="12" cy="12" r="8" fill="none" stroke="#fff" stroke-width="1"/>
    <path d="M12 6v6l4 3" fill="none" stroke="#fff" stroke-width="1.6" stroke-linecap="round"/>
  </svg>
  <table class="hours-table abs">
    <tr><td>Monday</td><td>8:00 AM</td><td class="dash">–</td><td>6:00 PM</td></tr>
    <tr><td>Tuesday</td><td>8:00 AM</td><td class="dash">–</td><td>6:00 PM</td></tr>
    <tr><td>Wednesday</td><td>8:00 AM</td><td class="dash">–</td><td>6:00 PM</td></tr>
    <tr><td>Thursday</td><td>8:00 AM</td><td class="dash">–</td><td>6:00 PM</td></tr>
    <tr><td>Friday</td><td>8:00 AM</td><td class="dash">–</td><td>6:00 PM</td></tr>
    <tr><td>Saturday</td><td>8:00 AM</td><td class="dash">–</td><td>6:00 PM</td></tr>
    <tr><td>Sunday</td><td>8:00 AM</td><td class="dash">–</td><td>6:00 PM</td></tr>
  </table>
  <a class="btn-appointment abs">Book an Appointment</a>
</aside>

<section class="card abs" style="left:81px;top:595px;width:196px;height:178px">
  <div class="card-head head-blue">Staff
    <svg class="card-icon" width="28" height="22" viewBox="0 0 28 22" aria-hidden="true">
      <circle cx="14" cy="5" r="3.6" fill="#fff"/><path d="M8 19c0-5 2.5-8 6-8s6 3 6 8z" fill="#fff"/>
      <circle cx="6" cy="8" r="2.8" fill="#fff"/><path d="M1 19c0-4 2-6.5 5-6.5 1.2 0 2 .3 2.6.8C7.5 15 7 17 7 19z" fill="#fff"/>
      <circle cx="22" cy="8" r="2.8" fill="#fff"/><path d="M27 19c0-4-2-6.5-5-6.5-1.2 0-2 .3-2.6.8C20.5 15 21 17 21 19z" fill="#fff"/>
    </svg>
  </div>
  <ul class="staff-list">
    <li>Dr.John Smith. MD</li><li>Dr.John Smith. MD</li><li>Dr.John Smith. MD</li><li>Dr.John Smith. MD</li><li>Dr.John Smith. MD</li>
  </ul>
  <a class="btn-small btn-blue" style="left:67px;top:151px;width:62px">View All</a>
</section>

<section class="card abs" style="left:293px;top:595px;width:196px;height:178px">
  <div class="card-head head-navy">Links
    <svg class="card-icon" width="22" height="22" viewBox="0 0 24 24" aria-hidden="true">
      <g fill="none" stroke="#fff" stroke-width="3" stroke-linecap="round">
        <path d="M10 14a4 4 0 0 0 5.7 0l4-4a4 4 0 0 0-5.7-5.7l-1.5 1.5"/>
        <path d="M14 10a4 4 0 0 0-5.7 0l-4 4a4 4 0 0 0 5.7 5.7l1.5-1.5"/>
      </g>
    </svg>
  </div>
  <ul class="link-list">
    <li><svg width="11" height="10" viewBox="0 0 11 10" aria-hidden="true"><path d="M1 5l3 3 6-7" fill="none" stroke="#8a8f99" stroke-width="1.6"/></svg>LTA Clinics</li>
    <li><svg width="11" height="10" viewBox="0 0 11 10" aria-hidden="true"><path d="M1 5l3 3 6-7" fill="none" stroke="#8a8f99" stroke-width="1.6"/></svg>LTA Clinics</li>
    <li><svg width="11" height="10" viewBox="0 0 11 10" aria-hidden="true"><path d="M1 5l3 3 6-7" fill="none" stroke="#8a8f99" stroke-width="1.6"/></svg>LTA Clinics</li>
    <li><svg width="11" height="10" viewBox="0 0 11 10" aria-hidden="true"><path d="M1 5l3 3 6-7" fill="none" stroke="#8a8f99" stroke-width="1.6"/></svg>LTA Clinics</li>
    <li><svg width="11" height="10" viewBox="0 0 11 10" aria-hidden="true"><path d="M1 5l3 3 6-7" fill="none" stroke="#8a8f99" stroke-width="1.6"/></svg>LTA Clinics</li>
  </ul>
  <a class="btn-small btn-sky" style="left:65px;top:151px;width:62px">View All</a>
</section>

<section class="newpatients abs">
  <h3>New Patients</h3>
  <svg class="abs" style="right:8px;top:6px" width="24" height="28" viewBox="0 0 24 28" aria-hidden="true">
    <g fill="none" stroke="#fff" stroke-width="1.4">
      <circle cx="9" cy="6" r="4"/><path d="M2 26V17c0-3 3-5 7-5"/>
      <rect x="12" y="12" width="9" height="13" rx="1"/><path d="M14 16h5M14 19h5M14 22h3"/>
    </g>
  </svg>
  <p>Accepting new patients</p>
  <a class="btn-contact abs">Contact us</a>
</section>

<section class="toolbox-panel abs">
  <a class="btn-toolbox abs">Physician Toolbox</a>
</section>

<section class="alerts-card card abs">
  <div class="card-head head-navy">Alerts
    <svg class="card-icon" width="28" height="24" viewBox="0 0 28 24" aria-hidden="true" style="top:8px">
      <path d="M14 1L27 23H1z" fill="#fff"/><rect x="12.7" y="8" width="2.6" height="8" fill="#2e4470"/><rect x="12.7" y="18" width="2.6" height="2.6" fill="#2e4470"/>
    </svg>
  </div>
  <div class="alert-item" style="top:56px">
    <h4>Alert Heasline 1</h4>
    <p>Ut wisi enim ad minim veniam, quis nostrud exerci tation ullamcorper suscipit lobortis nisl ut aliquip ex ea commodo consequat.</p>
  </div>
  <div class="alert-item" style="top:116px">
    <h4>Alert Heasline 2</h4>
    <p>Ut wisi enim ad minim veniam, quis nostrud exerci tation ullamcorper suscipit lobortis nisl ut aliquip ex ea commodo consequat. Ut wisi enim ad minim veniam, quis nostrud exerci tation ullamcorper suscipit lobortis nisl ut aliquip ex ea commodo consequat.</p>
  </div>
</section>

<section class="policies-card card abs">
  <div class="card-head head-blue">Clinic Policies
    <svg class="card-icon" width="26" height="30" viewBox="0 0 26 30" aria-hidden="true" style="top:5px">
      <path d="M6 1h12l6 6v20H6z" fill="#fff"/><path d="M10 9h10M10 13h10M10 17h10" stroke="#2196f3" stroke-width="1.5"/>
      <circle cx="6" cy="21" r="4.5" fill="#fff" stroke="#2196f3" stroke-width="1.2"/><path d="M3 25l-1 4 4-2 4 2-1-4" fill="#fff"/>
    </svg>
  </div>
  <ul class="policy-list">
    <li>01 .&nbsp; Late arrivals</li>
    <li>02 .&nbsp; Missed appointments</li>
    <li>03 .&nbsp; Fees for missed appointments</li>
    <li>04 .&nbsp; Referrals and follow-ups</li>
    <li>05 .&nbsp; Services not covered by RHC</li>
    <li>06 .&nbsp; Information for LTA patients</li>
    <li>07 .&nbsp; Medical Legal Reports</li>
  </ul>
  <a class="btn-small btn-sky" style="left:71px;top:188px;width:62px">View All</a>
</section>

<footer class="site-footer abs">
  <div class="footer-col abs" style="left:95px;top:20px">
    <h5>Our Clinic</h5>
    <ul><li>Mission</li><li>Services</li><li>Schedules</li><li>Policies</li></ul>
  </div>
  <span class="footer-rule" style="left:187px"></span>
  <div class="footer-col abs" style="left:234px;top:20px">
    <h5>Resources</h5>
    <ul><li>Our clinic</li><li>Mission</li><li>Services</li></ul>
  </div>
  <span class="footer-rule" style="left:334px"></span>
  <div class="footer-col abs" style="left:358px;top:20px">
    <h5>Hours of operation</h5>
    <table class="footer-hours">
      <tr><td>Monday</td><td>8:00 AM – 6:00 PM</td></tr>
      <tr><td>Tuesday</td><td>8:00 AM – 6:00 PM</td></tr>
      <tr><td>Wednesday</td><td>8:00 AM – 6:00 PM</td></tr>
      <tr><td>Thursday</td><td>8:00 AM – 6:00 PM</td></tr>
      <tr><td>Friday</td><td>8:00 AM – 6:00 PM</td></tr>
      <tr><td>Saturday</td><td>8:00 AM – 6:00 PM</td></tr>
      <tr><td>Sunday</td><td>8:00 AM – 6:00 PM</td></tr>
    </table>
  </div>
  <span class="footer-rule" style="left:527px"></span>
  <div class="footer-col abs" style="left:566px;top:20px">
    <h5 style="margin-left:5px">Contact us</h5>
    <ul class="footer-contact">
      <li><svg width="10" height="10" viewBox="0 0 24 24" aria-hidden="true"><path d="M6.6 10.8a15 15 0 0 0 6.6 6.6l2.2-2.2c.3-.3.7-.4 1-.2 1.1.4 2.3.6 3.6.6.6 0 1 .4 1 1V20c0 .6-.4 1-1 1C10.6 21 3 13.4 3 4c0-.6.4-1 1-1h3.5c.6 0 1 .4 1 1 0 1.3.2 2.5.6 3.6.1.3 0 .7-.2 1z" fill="#4aa8f5"/></svg>321-555-846</li>
      <li><svg width="10" height="8" viewBox="0 0 20 14" aria-hidden="true"><rect width="20" height="14" rx="1" fill="#4aa8f5"/><path d="M1 1l9 7 9-7" fill="none" stroke="#2e4470" stroke-width="1.5"/></svg>Clinicname@mediqo.com</li>
      <li><svg width="9" height="11" viewBox="0 0 18 24" aria-hidden="true"><path d="M9 0a9 9 0 0 0-9 9c0 6.8 9 15 9 15s9-8.2 9-15a9 9 0 0 0-9-9zm0 12.5A3.5 3.5 0 1 1 9 5.5a3.5 3.5 0 0 1 0 7z" fill="#4aa8f5"/></svg>123 Saqure mall , Lorwick,9,c</li>
    </ul>
  </div>
  <p class="copyright abs">© 2015 Copyright.ClinicName.com</p>
</footer>

</body>
</html>
```